Plovenworks business card

We need a modern business card - With our 4 colors - See web: www.plovenworks.dk

I have attached logo and som old business Cards we have - Lets Make the new ones shine...:-) -

Industry/Entity Type

Business

Requirements
Must have
• the logo with plovnworks only,

```html
<!DOCTYPE html>
<html lang="da">
<head>
<meta charset="utf-8">
<title>Plovenworks business card</title>
<link rel="stylesheet" href="https://fonts.googleapis.com/css2?family=Questrial&family=Arimo:wght@400;700&display=swap">
<style>
  :root {
    --stage: #1c1c1c;
    --card-dark: #2a2a2a;
    --card-light: #f3f3f3;
    --ink-soft: #777777;
    --ink-light: #d8d8d8;
    --brand-green: #8cc63f;
    --brand-orange: #e8831f;
    --brand-purple: #7b2d8e;
    --brand-magenta: #c3198b;
  }
  * { margin: 0; padding: 0; box-sizing: border-box; }
  html, body { width: 1200px; height: 873px; overflow: hidden; }
  body {
    background: var(--stage);
    display: flex;
    align-items: center;
    justify-content: center;
    gap: 40px;
    font-family: "Arimo", Arial, sans-serif;
  }
  .card {
    position: relative;
    width: 540px;
    height: 310px;
    overflow: hidden;
    box-shadow: 0 12px 30px rgba(0,0,0,.6);
  }
  .card-shape { position: absolute; inset: 0; width: 100%; height: 100%; }

  /* front */
  .card-front { background: var(--card-light); }
  .front-wordmark {
    position: absolute;
    top: 108px; left: 0; right: 0;
    display: flex; align-items: center; justify-content: center; gap: 14px;
  }
  .wordmark-dot { width: 22px; height: 22px; border-radius: 50%; background: var(--brand-green); }
  .wordmark-name {
    font-family: "Questrial", Arial, sans-serif;
    font-size: 30px;
    letter-spacing: 4px;
    color: var(--ink-light);
    line-height: 1;
  }
  .tagline {
    position: absolute;
    left: 318px; top: 196px;
    font-family: "Questrial", Arial, sans-serif;
    font-size: 15px;
    line-height: 1;
    letter-spacing: 1px;
    white-space: nowrap;
    color: var(--ink-soft);
    transform: rotate(-12deg);
    transform-origin: left bottom;
  }

  /* back */
  .card-back { background: var(--card-dark); }
  .back-wordmark {
    position: absolute;
    top: 62px; left: 0; right: 0;
    display: flex; align-items: center; justify-content: center; gap: 12px;
  }
  .back-wordmark .wordmark-name { color: #333; font-size: 27px; }
  .holder {
    position: absolute;
    left: 60px; top: 200px;
    text-align: right;
    width: 150px;
  }
  .holder-name { font-size: 21px; font-weight: 700; color: var(--brand-orange); }
  .holder-role { font-size: 13px; font-weight: 700; color: #fff; margin-top: 3px; }
  .divider {
    position: absolute;
    left: 240px; top: 178px;
    width: 2px; height: 70px;
    background: linear-gradient(var(--card-dark), var(--brand-purple), var(--card-dark));
  }
  .contacts {
    position: absolute;
    left: 268px; top: 170px;
    list-style: none;
    font-size: 14px;
    color: #f0f0f0;
  }
  .contacts li { display: flex; align-items: center; gap: 10px; height: 26px; white-space: nowrap; }
  .contact-icon { width: 16px; height: 16px; flex: none; }
  .contact-web { font-weight: 700; margin-top: 4px; }
  .contact-web .domain { color: var(--brand-green); }
  .address {
    position: absolute;
    left: 0; right: 0; bottom: 26px;
    text-align: center;
    font-size: 15px;
    font-weight: 700;
    color: var(--brand-magenta);
  }
</style>
</head>
<body>

  <section class="card card-front" aria-label="Business card front">
    <svg class="card-shape" viewBox="0 0 540 310" preserveAspectRatio="none" aria-hidden="true">
      <path d="M0 0 H540 V150 C420 235 220 255 0 215 Z" fill="var(--card-dark)"/>
    </svg>
    <div class="front-wordmark">
      <span class="wordmark-dot"></span>
      <span class="wordmark-name">plovnworks</span>
    </div>
    <p class="tagline">ideer der virker</p>
  </section>

  <section class="card card-back" aria-label="Business card back">
    <svg class="card-shape" viewBox="0 0 540 310" preserveAspectRatio="none" aria-hidden="true">
      <path d="M0 0 H540 V110 C440 180 250 190 0 140 Z" fill="var(--card-light)"/>
    </svg>
    <div class="back-wordmark">
      <span class="wordmark-dot"></span>
      <span class="wordmark-name">plovnworks</span>
    </div>

    <div class="holder">
      <p class="holder-name">Mette Lind</p>
      <p class="holder-role">Director</p>
    </div>
    <span class="divider" aria-hidden="true"></span>

    <ul class="contacts">
      <li>
        <svg class="contact-icon" viewBox="0 0 16 16" aria-hidden="true">
          <rect x="4" y="1" width="8" height="14" rx="1.5" fill="none" stroke="var(--brand-orange)" stroke-width="1.6"/>
          <line x1="7" y1="12.5" x2="9" y2="12.5" stroke="var(--brand-orange)" stroke-width="1.4"/>
        </svg>
        <span>0400 318 276</span>
      </li>
      <li>
        <svg class="contact-icon" viewBox="0 0 16 16" aria-hidden="true">
          <rect x="1" y="3" width="14" height="10" fill="var(--brand-orange)"/>
          <path d="M1 3 L8 9 L15 3" fill="none" stroke="var(--card-dark)" stroke-width="1.3"/>
        </svg>
        <span>info@plovenworks.dk</span>
      </li>
      <li class="contact-web"><span>www.<span class="domain">plovenworks</span>.dk</span></li>
    </ul>

    <p class="address">Solbakke Allé 14, 4000 Roskilde</p>
  </section>

</body>
</html>
```